Business Card Design for Occupational Medicine Start Up Company

We need to design a professional business card. We are a healthcare company providing occupational medicine services to blue collar industries. We are professional, efficient and high quality service providers.

Target Market(s)

Blue Collar Industry: Shipbuilding, Ports, Trucking Companies; The Executives and Safety Officers for these companies

Industry/Entity Type

Healthcare

Contact Information for Business Card

Logo, Name, Title, Email, Phone

Other font styles liked:
• Please match our Brand Guide

Requirements
Must have
• Our Company Colors and Logo

```html
<!DOCTYPE html>
<html lang="en">
<head>
<meta charset="utf-8">
<title>CrewWell Business Card</title>
<link href="https://fonts.googleapis.com/css2?family=Montserrat:wght@400;700&family=Roboto:wght@400&display=swap" rel="stylesheet">
<style>
  :root {
    --navy: #253a8f;
    --navy-deep: #1e2f78;
    --navy-soft: #2d45a3;
    --sky: #3aa3e0;
    --amber: #f2a93b;
    --ink: #1c1c2b;
    --paper: #ffffff;
    --stage: #e4e6ec;
    --faint-blue: #e9edf7;
    --faint-amber: #fdf3e4;
  }
  * { margin: 0; padding: 0; box-sizing: border-box; }
  html, body { width: 1200px; height: 900px; overflow: hidden; }
  body {
    background: var(--stage);
    display: flex;
    flex-direction: column;
    align-items: center;
    justify-content: center;
    gap: 56px;
    font-family: "Roboto", Arial, sans-serif;
  }
  .card {
    position: relative;
    width: 630px;
    height: 360px;
    border-radius: 22px;
    overflow: hidden;
    box-shadow: 0 6px 20px rgba(20, 30, 70, 0.18);
  }
  /* Front */
  .card-front { background: var(--paper); }
  .front-decoration {
    position: absolute;
    left: 250px;
    top: 70px;
    width: 360px;
    height: 300px;
    border-radius: 50%;
    background: radial-gradient(ellipse at 45% 45%, var(--faint-blue) 0%, var(--faint-blue) 45%, var(--faint-amber) 62%, rgba(255,255,255,0) 72%);
  }
  .wordmark {
    display: flex;
    align-items: center;
    gap: 10px;
    font-family: "Montserrat", Arial, sans-serif;
    font-weight: 700;
    letter-spacing: 0.06em;
  }
  .wordmark-dot { border-radius: 50%; flex: none; }
  .front-wordmark {
    position: absolute;
    left: 150px;
    top: 62px;
    font-size: 30px;
    color: var(--navy);
  }
  .front-wordmark .wordmark-dot { width: 30px; height: 30px; background: var(--navy); }
  .contact-list {
    position: absolute;
    left: 44px;
    top: 208px;
    list-style: none;
    font-size: 17px;
    color: var(--ink);
    line-height: 1.45;
  }
  .contact-list li { display: flex; align-items: center; gap: 8px; }
  .contact-list svg { width: 14px; height: 14px; fill: var(--navy); flex: none; }
  .holder {
    position: absolute;
    right: 60px;
    top: 226px;
    text-align: right;
  }
  .holder-name {
    font-family: "Montserrat", Arial, sans-serif;
    font-weight: 700;
    font-size: 30px;
    color: var(--navy);
    letter-spacing: 0.03em;
  }
  .holder-title {
    font-size: 16px;
    color: var(--ink);
    margin-top: 2px;
  }
  .accent-block {
    position: absolute;
    right: 0;
    top: 238px;
    width: 34px;
    height: 40px;
    background: var(--navy);
  }
  /* Back */
  .card-back { background: var(--navy); }
  .back-pattern {
    position: absolute;
    inset: 0;
    background: linear-gradient(135deg, var(--navy-soft) 0%, var(--navy) 50%, var(--navy-deep) 100%);
  }
  .back-wordmark {
    position: absolute;
    left: 50%;
    top: 50%;
    transform: translate(-50%, -50%);
    font-size: 40px;
    color: var(--paper);
    gap: 14px;
  }
  .back-wordmark .wordmark-dot { width: 38px; height: 38px; background: var(--paper); }
</style>
</head>
<body>

  <section class="card card-front">
    <div class="front-decoration" role="img" aria-label="Large faint brand symbol watermark in pale blue and amber"></div>

    <div class="wordmark front-wordmark">
      <span class="wordmark-dot"></span>
      <span class="wordmark-name">CREWWELL</span>
    </div>

    <ul class="contact-list">
      <li>
        <svg viewBox="0 0 24 24" aria-hidden="true"><path d="M6.6 10.8a15.1 15.1 0 0 0 6.6 6.6l2.2-2.2a1 1 0 0 1 1-.25 11.4 11.4 0 0 0 3.6.57 1 1 0 0 1 1 1V20a1 1 0 0 1-1 1A17 17 0 0 1 3 4a1 1 0 0 1 1-1h3.5a1 1 0 0 1 1 1c0 1.25.2 2.45.57 3.6a1 1 0 0 1-.25 1z"/></svg>
        (555)014 2290
      </li>
      <li>
        <svg viewBox="0 0 24 24" aria-hidden="true"><path d="M2 5h20v14H2zm2 2v.5l8 5 8-5V7l-8 5z"/></svg>
        info@crewwell.com
      </li>
      <li>
        <svg viewBox="0 0 24 24" aria-hidden="true"><circle cx="12" cy="12" r="10"/></svg>
        www.crewwell.com
      </li>
    </ul>

    <div class="holder">
      <p class="holder-name">MARTIN HALE</p>
      <p class="holder-title">Director</p>
    </div>
    <div class="accent-block"></div>
  </section>

  <section class="card card-back">
    <div class="back-pattern" role="img" aria-label="Repeating embossed brand symbol pattern in navy blue"></div>
    <div class="wordmark back-wordmark">
      <span class="wordmark-dot"></span>
      <span class="wordmark-name">CREWWELL</span>
    </div>
  </section>

</body>
</html>
```